Signage design for New Office Windows

Hi,
We need are needing some signage for our new office window. We are unsure exactly what we are wanting. We are an IT Consulting Company specializing in the medical centre.
We are not wanting anything too busy and wanting something that looks sleek yet doesnt look out of place with the building.
We have a lot of window space and are unsure at this stage what parts of it to use, so we open to suggestions.
Please see attached image of our office/building and the idea's that we had below that correspond with the attached:
Area 1: Dimensions - 450h x 650w - We were wanting a small sign to go on the wall at the front of our building. There is 4 x holes already drilled that we could install an aluminium sign to the wall – we were thinking we just have our Vorel for Medical logo (please see attached) as well as its website address on a sign here - vorel.tv
Area 2: Dimensions - 1690h x 635w - Front Door – probably need Quillora IT Consulting, address, phone, web and email details – no cold callers – appointment only
Address: 74 Marden Lane Kelso,
Phone: 1300 651 822
Website: www.quillora.com.au
Email: info@quillora.com.au
Area 3: Dimensions - 540h x 3600w – Currently white perspex, Has 3 x fluorescent bulbs above it – so could light something up at night-time – or we just leave white?
Area 4: This area consists of 3 x windows each of which dimensions are - 630h x 970w – 1 and 2 are facing the street, 3 is on a 45 degrees angle.
Area 5: We were hoping to use about a 3rd of this window and still have a functional window. 1/3 of the windows dimensions for each window is is 450h x 970w
With Area 4 and 5 we were thinking that in one of these sections we could perhaps list the services we offer? Please see back of business card attached for list of services we offer, and the other were thinking we could have our name/logo or something in the other section? We are open to suggestions. Please see logo attached also.
Area 6 Dimensions: 1760h x 665w – 2nd Door (will be closed to the public) – no idea what we could put on this door or if it needs anything?
We have just uploaded an image of the building with no text or anything on it so that you can add your designs to the office frontage so we can get an idea.
We have also added 2 x pictures that feature the office number that is displayed on our office. (74 sign 1 and 74 sign 2)
There are 2 x 74 Signs on Side of Building – Currently Clear Perspex with only 74 Number on it
1000h x 1225w
If you could do up a design keeping the 74 in it but perhaps incorporating our logo? Open to suggestions, but we would like the 74 to remain in the design.
We specialize in the medical sector so are also open to suggestions of incorporating the hearbeat into part of the design if it fits -
https://www.plenvask.com.au/search?q=heartbeat
We need some sort of flow between all the signage
It is possible that the windows may just be better with some sort of pattern? As we don’t want to overdo the signage.
In regards to colours we are quite open to using the colours in our logo, so Blue, Orange, Grey, Black, and White, but are also open to suggestions.
Looking forward to seeing what you can come up with
Cheers,
HI,
We have also added 2 x pictures that feature the office number that is displayed on our office.
1000h x 1225w
Thank you,
Reason: Some desings are close but there a still a few more things we would like to try/see.
Thanks,

```html
<!DOCTYPE html>
<html lang="en">
<head>
<meta charset="utf-8">
<title>Quillora IT Consulting – Window Banners</title>
<link rel="stylesheet" href="https://fonts.googleapis.com/css2?family=Orbitron:wght@600&family=Arimo:wght@700&display=swap">
<style>
  :root {
    --canvas: #ffffff;
    --navy-edge: #1b2745;
    --navy-mid: #2b4a78;
    --blue-glow: #3e6da3;
    --silver: #e4e6ea;
    --silver-dark: #b9bcc2;
    --brand-blue: #1f6fc4;
    --brand-orange: #e87a22;
    --grey-text: #9a9ca1;
  }
  * { margin: 0; padding: 0; box-sizing: border-box; }
  html, body { width: 1200px; height: 1000px; overflow: hidden; background: var(--canvas); }
  .canvas { position: relative; width: 1200px; height: 1000px; }

  .banner {
    position: absolute;
    left: 65px;
    width: 1082px;
    height: 161px;
    overflow: hidden;
  }
  .banner--mono { top: 249px; }
  .banner--colour { top: 605px; }

  .banner__backdrop {
    position: absolute; inset: 0;
    background:
      radial-gradient(ellipse 520px 200px at 52% 55%, var(--blue-glow) 0%, rgba(62,109,163,0) 100%),
      linear-gradient(90deg, var(--navy-edge) 0%, var(--navy-mid) 35%, var(--navy-mid) 65%, var(--navy-edge) 100%);
  }

  .banner__mark {
    position: absolute;
    left: 90px; top: 21px;
    width: 84px; height: 84px;
    border-radius: 10px;
    background: var(--silver);
  }
  .banner--colour .banner__mark { left: 105px; background: var(--brand-orange); }

  .banner__web {
    position: absolute;
    left: 28px; top: 118px;
    font-family: "Arimo", Arial, sans-serif;
    font-weight: 700;
    font-size: 21px;
    color: var(--silver);
    letter-spacing: 0.2px;
  }
  .banner--colour .banner__web { left: 38px; }

  .banner__divider {
    position: absolute;
    left: 334px; top: 11px;
    width: 2px; height: 112px;
    background: var(--silver-dark);
  }
  .banner--colour .banner__divider {
    left: 342px; top: 9px; width: 3px; height: 116px;
    background: var(--brand-orange);
  }

  .banner__name {
    position: absolute;
    right: 50px; top: 10px;
    font-family: "Orbitron", sans-serif;
    font-weight: 600;
    font-size: 78px;
    line-height: 1;
    letter-spacing: 2px;
    color: var(--silver);
  }
  .banner--colour .banner__name { top: 23px; color: var(--brand-blue); }

  .banner__tagline {
    position: absolute;
    right: 48px; top: 97px;
    font-family: "Arimo", Arial, sans-serif;
    font-weight: 700;
    font-size: 22px;
    letter-spacing: 12.5px;
    margin-right: -12.5px;
    color: var(--silver);
  }
  .banner--colour .banner__tagline { top: 110px; color: var(--grey-text); }
</style>
</head>
<body>
<main class="canvas">

  <section class="banner banner--mono" aria-label="Quillora IT Consulting banner, silver version">
    <div class="banner__backdrop" role="img" aria-label="Deep navy gradient backdrop with a faint repeated monogram pattern"></div>
    <div class="banner__mark"></div>
    <p class="banner__web">www.quillora.com.au</p>
    <div class="banner__divider"></div>
    <h1 class="banner__name">Quillora</h1>
    <p class="banner__tagline">IT CONSULTING</p>
  </section>

  <section class="banner banner--colour" aria-label="Quillora IT Consulting banner, colour version">
    <div class="banner__backdrop" role="img" aria-label="Deep navy gradient backdrop with a faint repeated monogram pattern"></div>
    <div class="banner__mark"></div>
    <p class="banner__web">www.quillora.com.au</p>
    <div class="banner__divider"></div>
    <h2 class="banner__name">Quillora</h2>
    <p class="banner__tagline">IT CONSULTING</p>
  </section>

</main>
</body>
</html>
```